NEW YORK Plumbing/utility company 10 year anniversary business card

Looking For simple back and front business card would like to include a few things in description
We offer 24/7 emergency service
residential
commercial
industrial
municipal
services offered
Plumbing
hydro excavation
hydro jetting
Well pumps
Sewer pumps
water mains
sewer mains

```html
<!DOCTYPE html>
<html lang="en">
<head>
<meta charset="utf-8">
<title>Millbrook Water &amp; Sewer – Business Card</title>
<link rel="stylesheet" href="https://fonts.googleapis.com/css2?family=Fira+Sans:wght@400;600;700&display=swap">
<style>
  :root {
    --blue: #1f78c1;
    --blue-light: #3f9fd9;
    --ink: #2f3338;
    --ink-soft: #4b5057;
    --card: #f7f8f9;
    --backdrop: #e7e9ec;
  }
  * { box-sizing: border-box; margin: 0; padding: 0; }
  html, body { width: 1200px; height: 1023px; overflow: hidden; }
  body {
    background: var(--backdrop);
    font-family: "Fira Sans", Arial, sans-serif;
    color: var(--ink);
    position: relative;
  }
  .card {
    position: absolute;
    width: 525px;
    height: 300px;
    background: var(--card);
    box-shadow: 0 2px 10px rgba(0,0,0,.12);
    overflow: hidden;
  }
  .card-frame {
    position: absolute;
    inset: 9px;
    border: 2px solid var(--blue-light);
  }
  .card-front { left: 50px; top: 360px; }
  .card-back  { left: 625px; top: 360px; }

  /* brand name block */
  .brand {
    position: absolute;
    display: flex;
    align-items: center;
    gap: 10px;
  }
  .brand-dot {
    width: 26px; height: 26px;
    border-radius: 50%;
    background: var(--blue);
    flex: none;
  }
  .brand-name {
    font-weight: 700;
    color: var(--blue);
    font-size: 21px;
    line-height: 1.1;
    letter-spacing: .4px;
    text-transform: uppercase;
  }
  .card-front .brand { left: 36px; top: 124px; }
  .card-back .brand  { left: 40px; top: 30px; }

  /* service lists */
  .offer {
    position: absolute;
    left: 282px;
    width: 212px;
  }
  .offer-emergency { top: 26px; }
  .offer-services  { top: 128px; }
  .offer-title {
    background: var(--blue);
    color: #fff;
    font-weight: 600;
    font-size: 16px;
    line-height: 20px;
    padding: 4px 11px;
    border-radius: 8px 8px 8px 0;
  }
  .offer-list { list-style: none; margin-top: 4px; padding-left: 6px; }
  .offer-list li {
    display: flex; align-items: center; gap: 7px;
    font-size: 12px; line-height: 15px; color: var(--ink-soft);
  }
  .tick { width: 11px; height: 11px; flex: none; }

  /* contact side */
  .divider {
    position: absolute;
    left: 30px; right: 30px; top: 104px;
    height: 2px; background: var(--blue-light);
  }
  .person { position: absolute; left: 40px; top: 114px; }
  .person-name { font-size: 21px; line-height: 25px; font-weight: 700; color: var(--ink); }
  .person-role { font-size: 12.5px; line-height: 16px; color: var(--blue-light); }
  .contact {
    position: absolute; left: 40px; top: 164px;
    list-style: none;
  }
  .contact li {
    display: flex; align-items: center; gap: 8px;
    font-size: 12px; line-height: 17px; color: var(--ink-soft);
  }
  .contact .address { display: block; margin-bottom: 3px; }
  .icon { width: 11px; height: 11px; flex: none; fill: var(--blue); }
</style>
</head>
<body>

<!-- Services side -->
<section class="card card-front">
  <div class="card-frame"></div>
  <div class="brand">
    <span class="brand-dot"></span>
    <span class="brand-name">Millbrook<br>Water &amp; Sewer</span>
  </div>

  <div class="offer offer-emergency">
    <h2 class="offer-title">24/7 Emergency Service</h2>
    <ul class="offer-list">
      <li><svg class="tick" viewBox="0 0 12 12"><circle cx="6" cy="6" r="5.2" fill="none" stroke="#1f78c1" stroke-width="1.3"/><path d="M3.5 6.2l1.7 1.7 3.3-3.4" fill="none" stroke="#1f78c1" stroke-width="1.4"/></svg>Residential</li>
      <li><svg class="tick" viewBox="0 0 12 12"><circle cx="6" cy="6" r="5.2" fill="none" stroke="#1f78c1" stroke-width="1.3"/><path d="M3.5 6.2l1.7 1.7 3.3-3.4" fill="none" stroke="#1f78c1" stroke-width="1.4"/></svg>Commercial</li>
      <li><svg class="tick" viewBox="0 0 12 12"><circle cx="6" cy="6" r="5.2" fill="none" stroke="#1f78c1" stroke-width="1.3"/><path d="M3.5 6.2l1.7 1.7 3.3-3.4" fill="none" stroke="#1f78c1" stroke-width="1.4"/></svg>Industrial</li>
      <li><svg class="tick" viewBox="0 0 12 12"><circle cx="6" cy="6" r="5.2" fill="none" stroke="#1f78c1" stroke-width="1.3"/><path d="M3.5 6.2l1.7 1.7 3.3-3.4" fill="none" stroke="#1f78c1" stroke-width="1.4"/></svg>Municipal</li>
    </ul>
  </div>

  <div class="offer offer-services">
    <h2 class="offer-title">Services Offered</h2>
    <ul class="offer-list">
      <li><svg class="tick" viewBox="0 0 12 12"><circle cx="6" cy="6" r="5.2" fill="none" stroke="#1f78c1" stroke-width="1.3"/><path d="M3.5 6.2l1.7 1.7 3.3-3.4" fill="none" stroke="#1f78c1" stroke-width="1.4"/></svg>Plumbing</li>
      <li><svg class="tick" viewBox="0 0 12 12"><circle cx="6" cy="6" r="5.2" fill="none" stroke="#1f78c1" stroke-width="1.3"/><path d="M3.5 6.2l1.7 1.7 3.3-3.4" fill="none" stroke="#1f78c1" stroke-width="1.4"/></svg>Hydro excavation</li>
      <li><svg class="tick" viewBox="0 0 12 12"><circle cx="6" cy="6" r="5.2" fill="none" stroke="#1f78c1" stroke-width="1.3"/><path d="M3.5 6.2l1.7 1.7 3.3-3.4" fill="none" stroke="#1f78c1" stroke-width="1.4"/></svg>Hydro jetting</li>
      <li><svg class="tick" viewBox="0 0 12 12"><circle cx="6" cy="6" r="5.2" fill="none" stroke="#1f78c1" stroke-width="1.3"/><path d="M3.5 6.2l1.7 1.7 3.3-3.4" fill="none" stroke="#1f78c1" stroke-width="1.4"/></svg>Well pumps</li>
      <li><svg class="tick" viewBox="0 0 12 12"><circle cx="6" cy="6" r="5.2" fill="none" stroke="#1f78c1" stroke-width="1.3"/><path d="M3.5 6.2l1.7 1.7 3.3-3.4" fill="none" stroke="#1f78c1" stroke-width="1.4"/></svg>Sewer pumps</li>
      <li><svg class="tick" viewBox="0 0 12 12"><circle cx="6" cy="6" r="5.2" fill="none" stroke="#1f78c1" stroke-width="1.3"/><path d="M3.5 6.2l1.7 1.7 3.3-3.4" fill="none" stroke="#1f78c1" stroke-width="1.4"/></svg>Water mains</li>
      <li><svg class="tick" viewBox="0 0 12 12"><circle cx="6" cy="6" r="5.2" fill="none" stroke="#1f78c1" stroke-width="1.3"/><path d="M3.5 6.2l1.7 1.7 3.3-3.4" fill="none" stroke="#1f78c1" stroke-width="1.4"/></svg>Sewer mains</li>
    </ul>
  </div>
</section>

<!-- Contact side -->
<section class="card card-back">
  <div class="card-frame"></div>
  <div class="brand">
    <span class="brand-dot"></span>
    <span class="brand-name">Millbrook<br>Water &amp; Sewer</span>
  </div>
  <div class="divider"></div>

  <div class="person">
    <p class="person-name">Your Name Here</p>
    <p class="person-role">Managing Director</p>
  </div>

  <ul class="contact">
    <li class="address">418 Alder Creek Road, Suite 12,<br>Kingston, New York 12401</li>
    <li><svg class="icon" viewBox="0 0 12 12"><path d="M2.5 1h2l1 2.6-1.3 1a6.5 6.5 0 0 0 3.2 3.2l1-1.3L11 7.5v2A1.5 1.5 0 0 1 9.5 11 8.5 8.5 0 0 1 1 2.5 1.5 1.5 0 0 1 2.5 1z"/></svg>(555) 014-2290</li>
    <li><svg class="icon" viewBox="0 0 12 12"><path d="M3.5 0.5h5a1 1 0 0 1 1 1v9a1 1 0 0 1-1 1h-5a1 1 0 0 1-1-1v-9a1 1 0 0 1 1-1zm0.5 1.5v7h4V2z"/></svg>(555) 014-2291</li>
    <li><svg class="icon" viewBox="0 0 12 12"><path d="M1 2.5h10v7H1zm1 1v.3l4 2.6 4-2.6v-.3zm0 1.5v3.5h8V5L6 7.6z"/></svg>youremail@youremail.com</li>
    <li><svg class="icon" viewBox="0 0 12 12"><path d="M6 0.8a5.2 5.2 0 1 0 0 10.4A5.2 5.2 0 0 0 6 0.8zm0 1.2c.7.8 1.1 1.9 1.2 3.3H4.8C4.9 3.9 5.3 2.8 6 2zM2.1 5.3a4 4 0 0 1 1.8-2.8 6.6 6.6 0 0 0-.8 2.8zm0 1.4h1a6.6 6.6 0 0 0 .8 2.8 4 4 0 0 1-1.8-2.8zM6 10c-.7-.8-1.1-1.9-1.2-3.3h2.4C7.1 8.1 6.7 9.2 6 10zm2.1-.5a6.6 6.6 0 0 0 .8-2.8h1a4 4 0 0 1-1.8 2.8zm.8-4.2a6.6 6.6 0 0 0-.8-2.8 4 4 0 0 1 1.8 2.8z"/></svg>www.yourwebsite.com</li>
  </ul>
</section>

</body>
</html>
```